Veltrona stationery design

Design stationery for us that fits with the colours of the logo. We are looking for letterheads, business cards etc. Something we can use for a prospectus and marketing presentations in power point. Must be completed in such a manner that it represents a corporate image for large enterprise clients and other large organisations. The company is a project assurance and monitoring company that works in all industries.

```html
<!DOCTYPE html>
<html lang="en">
<head>
<meta charset="UTF-8">
<title>Veltrona Business Card</title>
<link href="https://fonts.googleapis.com/css2?family=Montserrat:wght@400;500;700;800&display=swap" rel="stylesheet">
<style>
  :root {
    --navy: #0f2a52;
    --navy-deep: #0b2347;
    --orange: #f36b12;
    --orange-light: #ff8a1f;
    --ink: #1c1c1c;
    --rule: #8a93a3;
    --paper: #ffffff;
    --backdrop: #e6e7ea;
  }
  * { box-sizing: border-box; margin: 0; padding: 0; }
  html, body {
    width: 1200px; height: 1200px; overflow: hidden;
    background: var(--backdrop);
    font-family: "Montserrat", sans-serif;
  }
  .canvas { position: relative; width: 1200px; height: 1200px; }
  .card {
    position: absolute; left: 180px; width: 840px; height: 480px;
    border-radius: 34px; overflow: hidden;
    box-shadow: 0 10px 28px rgba(0,0,0,0.18);
  }
  .card-front { top: 70px; background: var(--paper); }
  .card-back { top: 640px; background: var(--navy-deep); border-bottom: 4px solid var(--orange); }

  .brand { display: flex; align-items: center; gap: 16px; }
  .brand-dot { width: 46px; height: 46px; border-radius: 50%; background: var(--orange); }
  .brand-name { font-weight: 800; letter-spacing: 2px; font-size: 46px; }

  .card-front .brand { position: absolute; left: 230px; top: 62px; }
  .card-front .brand-name { color: var(--navy); }

  .divider { position: absolute; left: 110px; right: 50px; top: 190px; height: 1px; background: var(--rule); }

  .identity { position: absolute; left: 62px; top: 222px; }
  .full-name { color: var(--orange); font-weight: 700; font-size: 44px; letter-spacing: 1px; line-height: 1; }
  .job-title { color: var(--ink); font-weight: 500; font-size: 22px; margin-top: 8px; letter-spacing: 1px; }
  .identity-rule { position: absolute; left: 62px; top: 318px; width: 330px; height: 1px; background: var(--rule); }

  .contact { list-style: none; position: absolute; font-size: 22px; color: var(--ink); font-weight: 500; }
  .contact li { display: flex; align-items: center; gap: 12px; margin-bottom: 10px; line-height: 1.15; }
  .contact svg { flex: 0 0 auto; }
  .contact-personal { left: 62px; top: 336px; }
  .contact-company { left: 470px; top: 212px; }
  .contact-company .address { font-size: 20px; }

  .band { position: absolute; left: 0; bottom: 0; width: 840px; height: 110px; }

  .card-back .brand { position: absolute; left: 50%; top: 50%; transform: translate(-50%, -50%); }
  .card-back .brand-name { color: var(--paper); font-size: 52px; }
  .card-back .brand-dot { width: 52px; height: 52px; }
</style>
</head>
<body>
<main class="canvas">

  <section class="card card-front" aria-label="Business card front">
    <div class="brand">
      <span class="brand-dot"></span>
      <span class="brand-name">VELTRONA</span>
    </div>

    <div class="divider"></div>

    <div class="identity">
      <p class="full-name">FULL NAME</p>
      <p class="job-title">TITLE</p>
    </div>
    <div class="identity-rule"></div>

    <ul class="contact contact-personal">
      <li>
        <svg width="24" height="24" viewBox="0 0 24 24"><path fill="var(--orange)" d="M6.6 10.8a15 15 0 0 0 6.6 6.6l2.2-2.2a1 1 0 0 1 1-.25 11.4 11.4 0 0 0 3.6.57 1 1 0 0 1 1 1V20a1 1 0 0 1-1 1A17 17 0 0 1 3 4a1 1 0 0 1 1-1h3.5a1 1 0 0 1 1 1c0 1.25.2 2.45.57 3.57a1 1 0 0 1-.25 1z"/></svg>
        <span>(000) 000 0000</span>
      </li>
      <li>
        <svg width="24" height="24" viewBox="0 0 24 24"><rect x="2" y="5" width="20" height="14" rx="1" fill="var(--orange)"/><path d="M2.5 6l9.5 7 9.5-7" stroke="#fff" stroke-width="1.6" fill="none"/></svg>
        <span>email@company.com</span>
      </li>
    </ul>

    <ul class="contact contact-company">
      <li>
        <svg width="26" height="26" viewBox="0 0 24 24" fill="none" stroke="var(--orange)" stroke-width="1.8"><circle cx="12" cy="12" r="9.5"/><ellipse cx="12" cy="12" rx="4" ry="9.5"/><path d="M2.5 12h19M4 7h16M4 17h16"/></svg>
        <span>www.company.com</span>
      </li>
      <li>
        <svg width="26" height="30" viewBox="0 0 24 28"><path fill="var(--orange)" d="M12 1a9 9 0 0 0-9 9c0 6.8 9 17 9 17s9-10.2 9-17a9 9 0 0 0-9-9zm0 12.5A3.5 3.5 0 1 1 12 6.5a3.5 3.5 0 0 1 0 7z"/></svg>
        <span class="address">123 Name Street, 000<br>Your City, 00000-000</span>
      </li>
    </ul>

    <svg class="band" viewBox="0 0 840 110" preserveAspectRatio="none" aria-hidden="true">
      <defs>
        <linearGradient id="orangeBand" x1="0" x2="1" y1="0" y2="0">
          <stop offset="0" stop-color="var(--orange)"/>
          <stop offset="1" stop-color="var(--orange-light)"/>
        </linearGradient>
      </defs>
      <polygon points="0,80 545,80 535,110 0,110" fill="url(#orangeBand)"/>
      <polygon points="555,0 840,0 840,110 545,110" fill="var(--navy)"/>
    </svg>
  </section>

  <section class="card card-back" aria-label="Business card back">
    <div class="brand">
      <span class="brand-dot"></span>
      <span class="brand-name">VELTRONA</span>
    </div>
  </section>

</main>
</body>
</html>
```